"Versipellis" Brand Label Design for Red Wine

Bruno Leitão Adegas is a Portuguese winemaking company born in the Douro Valley. Bruno Leitão, is a 7th generation winemaker and has a great reputation on making quality Portuguese wines,

Versipellis is latin for “opposite”, “contrary” and “in contradiction”. We would like to develop this brand by having an out of the box concept and design for the label based on this . We would like to go for something along the lines of the designs attached.

Also, this label must include:

• The brand name – “Versipellis”
• The Region of Origin – Douro
• The Appelation – Denominação de Origem Controlada
• The Type of Wine – “Vinho Tinto” and “Red Wine”
• The Vintage Year – 2020
• Use the bottle model from the technical sheet attached

We look forward to seeing your designs!

Industry/Entity Type

Wine and beverages

Requirements
Must have
• Out of the box concept

```html
<!DOCTYPE html>
<html lang="pt">
<head>
<meta charset="utf-8">
<title>Versipellis – Douro Red Wine Labels</title>
<link rel="stylesheet" href="https://fonts.googleapis.com/css2?family=Stardos+Stencil:wght@400;700&family=Oswald:wght@300;400;600&family=Questrial&family=Great+Vibes&display=swap">
<style>
  :root{
    --backdrop:#e4e4e4;
    --paper:#f4f4f3;
    --ink-dark:#262626;
    --ink-grey:#4a4a4a;
    --wine:#8e2a2c;
    --wine-soft:#a85456;
    --white:#ffffff;
  }
  *{margin:0;padding:0;box-sizing:border-box}
  html,body{width:1200px;height:1200px;overflow:hidden;background:var(--backdrop)}
  .stage{position:relative;width:1200px;height:1200px}

  .label{position:absolute;background:var(--paper);overflow:hidden;box-shadow:0 6px 24px rgba(0,0,0,.12)}

  /* front label */
  .label--front{left:50px;top:270px;width:560px;height:660px}
  .front__shade{position:absolute;inset:0}
  .front__brand{position:absolute;left:36px;top:70px;font-family:"Stardos Stencil",serif;font-weight:700;
    font-size:104px;line-height:.98;color:var(--wine-soft);letter-spacing:1px}
  .front__region{position:absolute;left:44px;top:380px;font-family:"Great Vibes",cursive;font-size:40px;color:var(--ink-grey)}
  .front__doc{position:absolute;left:36px;top:530px;font-family:"Oswald",sans-serif;font-weight:300;font-size:19px;line-height:1.35;color:var(--ink-grey)}
  .front__rule{position:absolute;left:0;top:592px;width:260px;height:2px;background:var(--ink-dark)}
  .front__volume{position:absolute;left:36px;top:606px;font-family:"Oswald",sans-serif;font-size:14px;color:var(--wine)}
  .front__vintage{position:absolute;right:30px;bottom:34px;width:210px;text-align:center;font-family:"Questrial",sans-serif}
  .vintage__year{font-size:54px;color:var(--white);letter-spacing:3px;line-height:1}
  .vintage__type{font-size:28px;color:var(--wine);border-top:3px solid var(--wine);border-bottom:3px solid var(--wine);margin:6px 0 4px;line-height:1.1;letter-spacing:1px}
  .vintage__local{font-size:22px;color:var(--white);letter-spacing:2px}

  /* back label */
  .label--back{left:660px;top:270px;width:490px;height:660px}
  .back__brand{position:absolute;left:0;right:0;top:46px;text-align:center;font-family:"Oswald",sans-serif;font-weight:600;
    font-size:86px;color:var(--wine-soft);letter-spacing:1px;line-height:1}
  .back__doc{position:absolute;left:0;right:0;top:150px;text-align:center;font-family:"Oswald",sans-serif;font-weight:300;font-size:22px;color:var(--ink-grey)}
  .back__band{position:absolute;left:8px;right:8px;top:200px;height:150px;background:var(--wine-soft);text-align:center;
    font-family:"Questrial",sans-serif;color:var(--white);padding-top:16px}
  .back__band .year{font-size:50px;letter-spacing:4px;line-height:1}
  .back__band .type{display:inline-block;font-size:30px;letter-spacing:2px;border-top:2px solid var(--white);border-bottom:2px solid var(--white);margin-top:6px;padding:0 4px;line-height:1.15}
  .back__band .local{font-size:22px;letter-spacing:3px;margin-top:4px}
  .back__pattern{position:absolute;left:14px;right:14px;top:372px;height:180px}
  .back__region{position:absolute;left:0;right:0;top:566px;text-align:center;font-family:"Questrial",sans-serif;font-size:24px;letter-spacing:4px;color:var(--ink-dark)}
  .back__bar{position:absolute;left:14px;right:14px;top:606px;height:30px;background:var(--ink-dark);color:var(--white);
    font-family:"Oswald",sans-serif;font-size:15px;letter-spacing:3px;text-align:center;line-height:30px}
</style>
</head>
<body>
<main class="stage">

  <section class="label label--front">
    <svg class="front__shade" width="560" height="660" viewBox="0 0 560 660" role="img" aria-label="Dark profile silhouette of a head facing right">
      <path d="M360 0 C390 70 420 200 400 300 C380 380 250 420 240 500 C232 570 260 630 300 660 L560 660 L560 0 Z" fill="var(--ink-dark)"/>
    </svg>
    <h1 class="front__brand">VERSI<br>PELLIS</h1>
    <p class="front__region">Douro</p>
    <p class="front__doc">Denominação de<br>Origem Controlada</p>
    <div class="front__rule"></div>
    <p class="front__volume">750ML | 13% ALC/VOL</p>
    <div class="front__vintage">
      <div class="vintage__year">2020</div>
      <div class="vintage__type">RED WINE</div>
      <div class="vintage__local">VINHO TINTO</div>
    </div>
  </section>

  <section class="label label--back">
    <h2 class="back__brand">VERSIPELLIS</h2>
    <p class="back__doc">Denominação de Origem Controlada</p>
    <div class="back__band">
      <div class="year">2020</div>
      <div class="type">RED WINE</div>
      <div class="local">VINHO TINTO</div>
    </div>
    <svg class="back__pattern" width="462" height="180" viewBox="0 0 462 180" role="img" aria-label="Pattern of line-drawn fish swimming one way, with a single red fish swimming the opposite way">
      <rect width="462" height="180" fill="#dcdcdc"/>
    </svg>
    <p class="back__region">DOURO</p>
    <div class="back__bar">750ML | 13% ALC/VOL</div>
  </section>

</main>
</body>
</html>
```